Delia Farrant

I need all of my logos on one card. I would like a burgundy back and Covera Summit and Tallowbrook insurance being the most prominent.
Phone Number 541-283-9150
Web:
www.Tallowbrookins.example
www.Covera Summit.example
www.Kettle-Insurance.example

```html
<!DOCTYPE html>
<html lang="en">
<head>
<meta charset="utf-8">
<title>Covera Summit – Business Card</title>
<link href="https://fonts.googleapis.com/css2?family=Cinzel:wght@500;600&family=Montserrat:wght@300;400&display=swap" rel="stylesheet">
<style>
  :root {
    --stage: #3d3f43;
    --card-white: #ffffff;
    --card-black: #151515;
    --burgundy: #6a1a2b;
    --burgundy-dark: #4c1020;
    --gold: #bfa23a;
    --ink: #141414;
    --soft-white: #f6f6f6;
    --title-grey: #d4d4d4;
  }
  * { box-sizing: border-box; margin: 0; padding: 0; }
  html, body { width: 1200px; height: 960px; overflow: hidden; }
  body { background: var(--stage); position: relative; font-family: "Montserrat", sans-serif; }

  .card {
    position: absolute;
    left: 250px;
    width: 700px;
    height: 400px;
    border-radius: 34px;
    overflow: hidden;
  }

  /* Back side */
  .card-back { top: 40px; background: var(--burgundy); }
  .back-pattern {
    position: absolute; inset: 0;
    background: linear-gradient(135deg, var(--burgundy) 0%, var(--burgundy-dark) 100%);
  }
  .back-mark {
    position: absolute; right: 120px; top: 238px; text-align: left;
  }
  .back-mark .brand-primary {
    font-family: "Cinzel", serif; font-weight: 600;
    font-size: 24px; letter-spacing: 1px; color: var(--gold);
    text-transform: uppercase; line-height: 1.1;
  }
  .back-mark .brand-secondary {
    font-family: "Cinzel", serif; font-weight: 600;
    font-size: 13px; letter-spacing: 1px; color: var(--soft-white);
    text-transform: uppercase; line-height: 1.3;
  }

  /* Front side */
  .card-front { top: 500px; background: var(--card-white); }
  .front-brand { position: absolute; left: 150px; top: 58px; }
  .front-brand .brand-primary {
    font-family: "Cinzel", serif; font-weight: 600;
    font-size: 54px; line-height: 1; letter-spacing: 2px;
    color: var(--gold); text-transform: uppercase; white-space: nowrap;
  }
  .front-brand .brand-secondary {
    font-family: "Cinzel", serif; font-weight: 600;
    font-size: 26px; line-height: 1; letter-spacing: 3px;
    color: var(--ink); text-transform: uppercase; white-space: nowrap;
    margin-top: 12px; margin-left: 40px;
  }

  .contact-band {
    position: absolute; left: 400px; top: 200px;
    width: 300px; height: 110px;
    background: var(--gold);
    padding: 12px 0 0 44px;
  }
  .contact-list { list-style: none; }
  .contact-list li {
    display: flex; align-items: center; gap: 9px;
    color: var(--soft-white);
    font-size: 13.5px; font-weight: 400;
    line-height: 21px; height: 21px; white-space: nowrap;
  }
  .contact-list svg { flex: none; }

  .name-band {
    position: absolute; left: 0; top: 282px;
    width: 430px; height: 88px;
    background: var(--card-black);
  }
  .name-pointer { position: absolute; left: 398px; top: 260px; }
  .name-block { position: absolute; right: 34px; top: 12px; text-align: right; }
  .person-name {
    font-family: "Cinzel", serif; font-weight: 500;
    font-size: 30px; line-height: 36px; color: var(--soft-white); letter-spacing: 1px;
  }
  .person-title {
    font-weight: 300; font-size: 19px; line-height: 26px;
    color: var(--title-grey); letter-spacing: 1px;
  }
</style>
</head>
<body>

  <section class="card card-back">
    <div class="back-pattern" role="img" aria-label="Faint repeating company name pattern across the burgundy card back"></div>
    <div class="back-mark">
      <div class="brand-primary">Covera Summit</div>
      <div class="brand-secondary">Tallowbrook Insurance</div>
    </div>
  </section>

  <section class="card card-front">
    <div class="front-brand">
      <div class="brand-primary">Covera Summit</div>
      <div class="brand-secondary">Tallowbrook Insurance</div>
    </div>

    <div class="contact-band">
      <ul class="contact-list">
        <li>
          <svg width="13" height="13" viewBox="0 0 24 24" aria-hidden="true"><path fill="#ffffff" d="M6.6 10.8a15.1 15.1 0 0 0 6.6 6.6l2.2-2.2a1 1 0 0 1 1-.25 11.4 11.4 0 0 0 3.6.57 1 1 0 0 1 1 1V20a1 1 0 0 1-1 1A17 17 0 0 1 3 4a1 1 0 0 1 1-1h3.5a1 1 0 0 1 1 1c0 1.25.2 2.45.57 3.57a1 1 0 0 1-.25 1z"/></svg>
          <span>541-283-9150</span>
        </li>
        <li>
          <svg width="13" height="13" viewBox="0 0 24 24" aria-hidden="true"><circle cx="12" cy="12" r="10" fill="#ffffff"/><circle cx="12" cy="12" r="4" fill="none" stroke="#bfa23a" stroke-width="2.5"/></svg>
          <span>www.Tallowbrookins.example</span>
        </li>
        <li>
          <svg width="13" height="13" viewBox="0 0 24 24" aria-hidden="true"><circle cx="12" cy="12" r="10" fill="#ffffff"/><circle cx="12" cy="12" r="4" fill="none" stroke="#bfa23a" stroke-width="2.5"/></svg>
          <span>www.Covera Summit.example</span>
        </li>
        <li>
          <svg width="13" height="13" viewBox="0 0 24 24" aria-hidden="true"><circle cx="12" cy="12" r="10" fill="#ffffff"/><circle cx="12" cy="12" r="4" fill="none" stroke="#bfa23a" stroke-width="2.5"/></svg>
          <span>www.Kettle-Insurance.example</span>
        </li>
      </ul>
    </div>

    <div class="name-band">
      <div class="name-block">
        <div class="person-name">YOUR NAME</div>
        <div class="person-title">YOUR TITLE</div>
      </div>
    </div>

    <svg class="name-pointer" width="32" height="24" viewBox="0 0 32 24" aria-hidden="true">
      <polygon points="2,0 32,0 32,22" fill="#ffffff"/>
    </svg>
  </section>

</body>
</html>
```